Smile club flyer design

I am launching an office smile club and would like a design that sits my branding and that is appealing to customers. I have a design (I need a new one) that has all the information.
My website is maplecrestdentalcarewv.com
Brand color is green. The design can be any color

Target Market(s)

Ages 30+

Industry/Entity Type

Dental

Font styles to use
Serif

Requirements
Must have
• Appealing to patients

```html
<!DOCTYPE html>
<html lang="en">
<head>
<meta charset="utf-8">
<title>Maplecrest Dental Care – Smile Club Membership</title>
<link rel="stylesheet" href="https://fonts.googleapis.com/css2?family=DM+Serif+Text&family=Inter:wght@400;500;600;700;800&display=swap">
<style>
  :root{
    --teal:#3db59f;
    --teal-dark:#2a9f8a;
    --teal-deep:#1f8f7c;
    --brand-green:#2c8a3c;
    --sky:#4fc1ea;
    --sky-pale:#d4eff6;
    --ice:#eaf7f8;
    --card:#f3fbfa;
    --ink:#2a2f33;
    --grey:#5d6366;
    --white:#ffffff;
  }
  *{box-sizing:border-box;margin:0;padding:0}
  html,body{width:939px;height:1200px;overflow:hidden;background:#fff}
  body{font-family:"Inter",Arial,sans-serif;color:var(--ink)}
  .flyer{position:relative;width:939px;height:1200px;overflow:hidden;
    background:linear-gradient(160deg,#cfeef4 0%,#eef8f6 30%,#f4fbf4 55%,#e8f6f7 100%)}
  .waves{position:absolute;inset:0;width:939px;height:1200px}
  .abs{position:absolute}

  .brand{left:0;right:0;top:58px;text-align:center;font-family:"DM Serif Text",Georgia,serif;
    font-size:44px;color:var(--brand-green);letter-spacing:.5px}
  .intro{left:0;right:0;top:152px;text-align:center;font-family:"DM Serif Text",Georgia,serif;
    font-size:68px;line-height:1;color:var(--teal);font-weight:400}
  .banner{left:54px;top:232px;width:830px;height:76px;border-radius:8px;
    background:linear-gradient(180deg,#47bea8,#34ab95);box-shadow:0 4px 8px rgba(0,0,0,.12);
    display:flex;align-items:center;justify-content:center;color:#fff;font-weight:700;font-size:55px;letter-spacing:.5px}
  .tagline{left:0;right:0;top:320px;text-align:center;font-weight:700;font-size:20px;color:var(--grey);letter-spacing:1.4px}

  .plan{top:369px;width:264px;height:375px;border-radius:12px;background:var(--card);overflow:hidden;
    box-shadow:0 4px 12px rgba(40,110,120,.12)}
  .plan-head{position:absolute;left:0;right:0;top:0;height:150px;
    background:linear-gradient(180deg,#4dbfea 0%,#8ad6f0 45%,#d8f0f2 100%)}
  .plan-name{position:absolute;left:0;right:0;top:16px;text-align:center;color:#fff;font-size:22px;line-height:27px;font-weight:400}
  .plan-name b{font-weight:700;display:block}
  .dome{position:absolute;left:35px;top:82px;width:194px;height:108px;border-radius:97px 97px 0 0;
    background:linear-gradient(180deg,#4cc0aa,#2fa790);color:#fff;text-align:center;padding-top:18px}
  .dome .price{font-size:56px;font-weight:800;line-height:1}
  .dome .per{font-size:18px;font-weight:500;margin-top:4px}
  .features{position:absolute;left:22px;right:14px;top:222px;list-style:none}
  .features li{position:relative;padding-left:18px;font-size:15px;line-height:19px;color:#3a4044;margin-bottom:7px}
  .features li::before,.perks li::before{content:"";position:absolute;left:0;top:4px;width:10px;height:10px;border:1.5px solid var(--teal);border-radius:50%}
  .features li::after,.perks li::after{content:"";position:absolute;left:4px;top:6px;width:3px;height:5px;border:solid var(--teal);border-width:0 1.5px 1.5px 0;transform:rotate(45deg)}

  .package{left:60px;top:792px;width:450px;height:178px;border-radius:10px;background:rgba(255,255,255,.85);
    box-shadow:0 4px 12px rgba(40,110,120,.12)}
  .new-tag{left:58px;top:775px;width:102px;height:38px;border-radius:6px;background:var(--teal);color:#fff;
    font-weight:700;font-size:22px;display:flex;align-items:center;justify-content:center}
  .pkg-title{left:80px;top:824px;font-size:24px;line-height:30px;color:var(--ink);font-weight:400}
  .pkg-title b{display:block;font-weight:700}
  .pkg-price{left:333px;top:806px;width:192px;height:68px;border-radius:6px;background:var(--teal);color:#fff;
    font-weight:800;font-size:56px;display:flex;align-items:center;justify-content:center}
  .pkg-per{left:333px;top:876px;width:192px;text-align:center;color:var(--teal-dark);font-weight:600;font-size:18px}
  .perks{left:80px;top:910px;list-style:none}
  .perks li{position:relative;padding-left:20px;font-weight:600;font-size:16.5px;line-height:20px;margin-bottom:9px}

  .join{left:564px;top:796px}
  .join span{display:block;width:max-content;color:#fff;font-weight:800;font-size:28px;line-height:38px;padding:0 10px;margin-bottom:4px;
    clip-path:polygon(0 0,100% 0,calc(100% - 14px) 100%,0 100%)}
  .join .j1{background:var(--sky);padding-right:30px}
  .join .j2{background:var(--teal-dark);padding-right:24px}
  .join .j3{background:var(--teal-dark);padding-right:30px}
  .phone{left:565px;top:925px;display:flex;align-items:center;gap:10px;font-weight:700;font-size:31px;color:var(--ink)}
  .phone i{width:30px;height:30px;border-radius:50%;background:var(--teal-dark);display:block}

  .finance{left:68px;top:1006px;width:420px;height:40px;border-radius:20px;background:var(--teal);color:#fff;
    font-weight:700;font-size:17.5px;display:flex;align-items:center;padding-left:26px;letter-spacing:.3px}
  .partners{left:455px;top:999px;width:415px;height:54px;border-radius:27px;background:#fff;
    box-shadow:0 3px 8px rgba(0,0,0,.15);display:flex;align-items:center;justify-content:center;gap:22px;
    font-weight:700;font-size:28px;color:var(--ink)}
  .partners .sep{width:2px;height:28px;background:#333}
  .plans-note{left:523px;top:1053px;width:300px;height:34px;background:#7ecff0;color:#fff;font-weight:700;font-size:18px;
    display:flex;align-items:center;justify-content:center;letter-spacing:.3px}
  .fee{left:89px;top:1060px;font-size:15px;color:var(--ink)}

  .footer{top:1136px;color:#fff;font-size:18px;display:flex;align-items:center;gap:8px}
  .footer.web{left:68px}
  .footer.mail{right:69px}
</style>
</head>
<body>
<main class="flyer">
  <svg class="waves" viewBox="0 0 939 1200" aria-hidden="true">
    <path d="M0 440 C200 380 500 470 939 420 L939 800 L0 800 Z" fill="#d3eef6" opacity=".75"/>
    <path d="M0 520 C250 470 600 560 939 500 L939 800 L0 800 Z" fill="#bfe6f2" opacity=".5"/>
    <path d="M0 1000 C300 1030 650 980 939 860 L939 1200 L0 1200 Z" fill="#d9f1f6"/>
    <path d="M0 1080 C330 1110 690 1040 939 900 L939 1200 L0 1200 Z" fill="#2a9f8a"/>
    <path d="M0 1095 C330 1125 700 1070 939 940 L939 1200 L0 1200 Z" fill="#3db59f"/>
  </svg>

  <div class="abs brand">Maplecrest Dental Care</div>
  <h1 class="abs intro">Introducing</h1>
  <div class="abs banner">SMILE CLUB MEMBERSHIP</div>
  <p class="abs tagline">AFFORDABLE DENTAL CARE — NO INSURANCE REQUIRED</p>

  <section class="abs plan" style="left:54px">
    <div class="plan-head"></div>
    <h2 class="plan-name">CORE CARE<b>PREVENTIVE</b></h2>
    <div class="dome"><div class="price">$39</div><div class="per">PER MONTH</div></div>
    <ul class="features">
      <li>Comprehensive Annual Exam</li>
      <li>2x Professional Cleanings per Year</li>
      <li>Routine Bitewing X-rays</li>
      <li>10% Savings on Treatment</li>
    </ul>
  </section>

  <section class="abs plan" style="left:338px">
    <div class="plan-head"></div>
    <h2 class="plan-name">BRIGHT<b>COSMETIC</b></h2>
    <div class="dome"><div class="price">$59</div><div class="per">PER MONTH</div></div>
    <ul class="features">
      <li>Annual In-Office Whitening (Top &amp; Bottom)</li>
      <li>Custom Whitening Trays</li>
      <li>15% Savings on Elective Treatment</li>
    </ul>
  </section>

  <section class="abs plan" style="left:621px">
    <div class="plan-head"></div>
    <h2 class="plan-name">CORE CARE<b>PREVENTIVE</b></h2>
    <div class="dome"><div class="price">$89</div><div class="per">PER MONTH</div></div>
    <ul class="features">
      <li>3-4 Perio Maintenance Visits per Year</li>
      <li>1 Comprehensive Exam</li>
      <li>Diagnostic X-rays</li>
      <li>15% Savings on Restorative &amp; Elective Care</li>
    </ul>
  </section>

  <div class="abs package"></div>
  <div class="abs new-tag">NEW</div>
  <h3 class="abs pkg-title">SMILE REFRESH<b>PACKAGE</b></h3>
  <div class="abs pkg-price">$499</div>
  <div class="abs pkg-per">PER MONTH</div>
  <ul class="abs perks">
    <li>Cleaning + Comprehensive Exam + Whitening</li>
    <li>Limited Time Offer</li>
  </ul>

  <div class="abs join"><span class="j1">JOIN</span><span class="j2">SMILE CLUB</span><span class="j3">TODAY!</span></div>
  <div class="abs phone"><i></i>(304) 555-0148</div>

  <div class="abs finance">FLEXIBLE FINANCING FOR TREATMENT</div>
  <div class="abs partners"><span>Evenfield</span><span class="sep"></span><span>Tallora</span></div>
  <div class="abs plans-note">PAYMENT PLANS AVAILABLE</div>
  <p class="abs fee">*$49 Lifetime Activation Fee (Non-Refundable)</p>

  <div class="abs footer web">
    <svg width="14" height="14" viewBox="0 0 14 14" fill="none" stroke="#fff" stroke-width="1.2"><circle cx="7" cy="7" r="6"/><ellipse cx="7" cy="7" rx="2.6" ry="6"/><path d="M1 7h12"/></svg>
    www.maplecrestdentalcarewv.com
  </div>
  <div class="abs footer mail">
    <svg width="16" height="12" viewBox="0 0 16 12" fill="none" stroke="#fff" stroke-width="1.2"><rect x=".6" y=".6" width="14.8" height="10.8" rx="1"/><path d="M1 1l7 6 7-6"/></svg>
    info@maplecrestdentalcare.com
  </div>
</main>
</body>
</html>
```